Business card for a "family office" company

Please provide professional looking business card designs, incorporating the attached logo and below details. Harrowmere Holdings Pty Ltd is a family office / financial investment company. We are looking for a modern, professional and contemporary card design.

Industry/Entity Type

Finance

Contact Information for Business Card

Name: Dean Mollick
Title: Director
Company: Harrowmere Holdings Pty Ltd
Email: harrowdean@quillnet.example
Mobile: 0462 735 418
Address: 4/312 Barnaby Parade, Fernvale WA 6990, Australia

Requirements
Must have
• All details above and the logo. logo only on back side. incorporate colours of logo
Nice to have
• up to you
Should not have
• ?

```html
<!DOCTYPE html>
<html lang="en">
<head>
<meta charset="utf-8">
<title>Harrowmere Holdings – Business Card</title>
<link rel="stylesheet" href="https://fonts.googleapis.com/css2?family=Cinzel:wght@500&family=Pacifico&family=Questrial&display=swap">
<style>
  :root {
    --stage: #5f5f5f;
    --card: #ffffff;
    --pattern-light: #f4f3f8;
    --pattern-tone: #e9e8f0;
    --navy: #241a5a;
    --violet: #3a2fa0;
    --ink: #1c1c1c;
  }
  * { box-sizing: border-box; margin: 0; padding: 0; }
  html, body { width: 1200px; height: 398px; overflow: hidden; background: var(--stage); }
  .stage { position: relative; width: 1200px; height: 398px; }

  .card { position: absolute; top: 11px; width: 563px; height: 374px; background: var(--card); overflow: hidden; }
  .card--front { left: 11px; border: 1px solid #222; }
  .card--back { left: 624px; }

  .front-texture { position: absolute; inset: 0;
    background: linear-gradient(180deg, var(--pattern-light), var(--pattern-tone)); }

  .wordmark { position: absolute; left: 0; right: 0; text-align: center; color: var(--navy);
    font-family: "Cinzel", serif; font-weight: 500; }
  .wordmark__main { display: block; font-size: 46px; line-height: 1; letter-spacing: 1px; }
  .wordmark__sub { display: block; font-size: 20px; line-height: 1; letter-spacing: 10px; margin-top: 10px; padding-left: 10px; }
  .card--front .wordmark { top: 12px; }

  .person { position: absolute; left: 0; right: 0; top: 100px; text-align: center;
    font-family: "Pacifico", cursive; color: var(--violet); font-size: 33px; line-height: 1.55; }

  .contacts { position: absolute; left: 0; top: 248px; list-style: none;
    font-family: "Questrial", sans-serif; color: var(--ink); font-size: 15px; }
  .contact { display: flex; align-items: center; height: 38px; margin-bottom: 4px; }
  .contact__icon { width: 34px; height: 34px; border-radius: 50%; background: var(--navy);
    display: flex; align-items: center; justify-content: center; margin-right: 12px; flex: none; }
  .contact__icon svg { width: 20px; height: 20px; fill: none; stroke: #fff; stroke-width: 1.6;
    stroke-linecap: round; stroke-linejoin: round; }

  .brand-block { position: absolute; left: 222px; top: 60px; width: 120px; height: 120px; background: var(--navy); }
  .card--back .wordmark { top: 206px; }
  .card--back .wordmark__main { font-size: 48px; }
  .card--back .wordmark__sub { margin-top: 12px; }
</style>
</head>
<body>
<main class="stage">
  <section class="card card--front">
    <div class="front-texture" role="img" aria-label="Faint repeating brand pattern in pale lavender"></div>
    <div class="wordmark">
      <span class="wordmark__main">Harrowmere</span>
      <span class="wordmark__sub">Holdings</span>
    </div>
    <div class="person">
      <p class="person__name">Dean Mollick</p>
      <p class="person__title">Director</p>
    </div>
    <ul class="contacts">
      <li class="contact">
        <span class="contact__icon"><svg viewBox="0 0 24 24"><rect x="3" y="6" width="18" height="13" rx="1"/><path d="M3 7l9 7 9-7"/></svg></span>
        harrowdean@quillnet.example
      </li>
      <li class="contact">
        <span class="contact__icon"><svg viewBox="0 0 24 24"><path d="M6 3h3l2 5-2 1.5a11 11 0 0 0 5.5 5.5L16 13l5 2v3a2 2 0 0 1-2 2A16 16 0 0 1 4 5a2 2 0 0 1 2-2z"/></svg></span>
        0462 735 418
      </li>
      <li class="contact">
        <span class="contact__icon"><svg viewBox="0 0 24 24"><path d="M12 21s-6-6.2-6-11a6 6 0 0 1 12 0c0 4.8-6 11-6 11z"/><circle cx="12" cy="10" r="2.2"/></svg></span>
        4/312 Barnaby Parade, Fernvale WA 6990, Australia
      </li>
    </ul>
  </section>

  <section class="card card--back">
    <div class="brand-block"></div>
    <div class="wordmark">
      <span class="wordmark__main">Harrowmere</span>
      <span class="wordmark__sub">Holdings</span>
    </div>
  </section>
</main>
</body>
</html>
```